Bramble Wren Childcare centre needs a new LED outdoor banner

We need a new outdoor banner for our pre-school. It needs to be around 2440 mm x 1220 mm. It will be lit at night so I need it to stand out. I'm looking for a modern upbeat design. It will have my logo in the middle which is a graduation teddy bear with our name and phone number on it. I'm happy to experiment with different design options as mine is 20 years old. It needs to be colorful, inviting and very "in your face" and child friendly. It will be located near the fence of the property so it will be seen by cars driving by at a speed of around 50KM/H. So it needs to be clear, big bold fonts and bright colors. Thank you!

```html
<!DOCTYPE html>
<html lang="en">
<head>
<meta charset="utf-8">
<title>Bramble Wren Childcare Centre – Outdoor Banner</title>
<link rel="stylesheet" href="https://fonts.googleapis.com/css2?family=Fredoka:wght@700&family=Roboto:wght@900&display=swap">
<style>
  :root {
    --page: #ffffff;
    --magenta: #e5198a;
    --magenta-glow: #f25aae;
    --magenta-deep: #b80f6c;
    --sky: #3fb6ea;
    --sky-deep: #229ad8;
    --emblem-top: #9b3fb4;
    --emblem-mid: #6a6fd0;
    --emblem-low: #2f9bdc;
    --white: #ffffff;
  }
  * { box-sizing: border-box; margin: 0; padding: 0; }
  html, body {
    width: 1200px;
    height: 933px;
    overflow: hidden;
    background: var(--page);
  }
  .canvas {
    position: relative;
    width: 1200px;
    height: 933px;
  }
  .banner {
    position: absolute;
    left: 50px;
    top: 191px;
    width: 1100px;
    height: 550px;
    overflow: hidden;
    background: radial-gradient(ellipse 60% 70% at 50% 30%, var(--magenta-glow), var(--magenta) 70%);
    box-shadow: 0 4px 18px rgba(0, 0, 0, 0.12);
  }
  .banner__band {
    position: absolute;
    left: 0;
    top: 297px;
    width: 100%;
    height: 253px;
    background: linear-gradient(180deg, var(--sky), var(--sky-deep));
  }
  .emblem {
    position: absolute;
    left: 270px;
    top: 20px;
    width: 560px;
    height: 290px;
    border-radius: 280px 280px 0 0;
    background: linear-gradient(180deg, var(--emblem-top), var(--emblem-mid) 55%, var(--emblem-low));
    opacity: 0.85;
  }
  .brand__word {
    position: absolute;
    top: 160px;
    font-family: "Fredoka", sans-serif;
    font-weight: 700;
    font-size: 100px;
    line-height: 1;
    color: var(--white);
    white-space: nowrap;
  }
  .brand__word--first {
    right: 665px;
    text-align: right;
  }
  .brand__word--second {
    left: 660px;
  }
  .tagline {
    position: absolute;
    left: 50%;
    top: 280px;
    transform: translateX(-50%);
    padding: 6px 34px 10px;
    border-radius: 40px;
    background: var(--white);
    font-family: "Fredoka", sans-serif;
    font-weight: 700;
    font-size: 56px;
    line-height: 1;
    color: var(--sky-deep);
    white-space: nowrap;
  }
  .contact {
    position: absolute;
    left: 50px;
    top: 380px;
    display: flex;
    align-items: center;
    gap: 60px;
  }
  .contact__icon {
    width: 115px;
    height: 125px;
    flex: none;
  }
  .contact__text {
    font-family: "Roboto", sans-serif;
    font-weight: 900;
    font-size: 104px;
    line-height: 1;
    color: var(--white);
    white-space: nowrap;
    text-shadow: 0 3px 0 var(--magenta-deep);
  }
</style>
</head>
<body>
  <main class="canvas">
    <section class="banner" aria-label="Bramble Wren Childcare Centre outdoor banner">
      <div class="banner__band"></div>

      <div class="emblem" role="img" aria-label="Space for the centre's emblem: a rainbow arch with a teddy bear in a graduation cap"></div>

      <h1 class="brand">
        <span class="brand__word brand__word--first">Bramble</span>
        <span class="brand__word brand__word--second">Wren</span>
      </h1>

      <p class="tagline">Childcare Centre</p>

      <div class="contact">
        <svg class="contact__icon" viewBox="0 0 120 130" aria-hidden="true">
          <rect x="6" y="6" width="108" height="118" rx="30" fill="var(--white)"/>
          <path d="M40 24 c-10 6 -16 18 -14 34 c3 22 18 42 38 50 c10 4 20 2 26 -6 l-14 -16 c-4 3 -8 4 -12 2 c-8 -5 -14 -15 -16 -24 c-1 -4 1 -8 5 -10 z"
                fill="var(--magenta)"/>
        </svg>
        <p class="contact__text">Call 9555-0142</p>
      </div>
    </section>
  </main>
</body>
</html>
```